Business card for a Exhibition booth fabrication company

Hi. My company would like to change our corporate name card. We are an events and Exhibition stand builder company. We would like our corporate name card to resonate what we do. I need someone to create something unique that relates to the industry that I am in. The graphic designer should be creative to incorporate the elements of my industry and try to blend in well in the design of the card. Our aim is to ensure that we are unique and our card can look different from our competitors.
Updates

The decision maker was very busy and didnt had time to make this decision

Target Market(s)

Marketing and events manager from all companies

Contact Information for Business Card

The business card should have the following details:
Name
Job Title
Email
Website

Colors

Designer to choose colors to be used in the design.

Requirements
Must have
• The card must be look something that is relevant to the service that I am providing. My website is: www.velmora-builds.com
• You can see my website to get more information on what service that I am doing
Nice to have
• On the back of my card, I would like to have a globe image with the incorporation of my company logo. This is to indicate that my services can be done in any part of the world.

```html
<!DOCTYPE html>
<html lang="en">
<head>
<meta charset="utf-8">
<title>Velmora Builds – Business Card</title>
<link rel="stylesheet" href="https://fonts.googleapis.com/css2?family=Open+Sans:wght@400;600;700&display=swap">
<style>
  :root {
    --bg: #e8e5e2;
    --paper: #ffffff;
    --charcoal: #4a4a4c;
    --charcoal-light: #5a5a5d;
    --red: #e3151d;
    --text-light: #ffffff;
    --text-muted: #d9d9d9;
    --brand-grey: #5b5b5e;
  }
  * { box-sizing: border-box; margin: 0; padding: 0; }
  html, body {
    width: 1200px; height: 997px; overflow: hidden;
    background: var(--bg);
    font-family: "Open Sans", Arial, sans-serif;
  }
  .card {
    position: absolute;
    width: 520px; height: 298px;
    overflow: hidden;
    box-shadow: 0 6px 18px rgba(0,0,0,0.12);
  }
  .card-front { left: 60px; top: 190px; background: var(--paper); }
  .card-back { left: 620px; top: 510px; background: var(--charcoal); }
  .card-shape { position: absolute; inset: 0; }

  .brand {
    position: absolute;
    display: flex; align-items: center; gap: 10px;
    font-weight: 700; letter-spacing: 2px; text-transform: uppercase;
  }
  .brand-dot { width: 22px; height: 22px; border-radius: 50%; background: var(--red); }
  .card-front .brand { left: 200px; top: 34px; font-size: 18px; color: var(--brand-grey); }
  .card-back .brand { left: 50%; top: 50%; transform: translate(-50%, -50%); font-size: 26px; color: var(--text-light); gap: 14px; }
  .card-back .brand-dot { width: 30px; height: 30px; }

  .holder {
    position: absolute; left: 48px; top: 190px;
    color: var(--text-light); font-size: 13px; line-height: 1.45;
  }
  .holder-name { font-weight: 700; text-transform: uppercase; font-size: 14px; }
  .holder-title { color: var(--text-muted); }
  .divider {
    position: absolute; left: 205px; top: 178px; width: 1px; height: 90px;
    background: rgba(255,255,255,0.35);
  }
  .contact-list {
    position: absolute; left: 222px; top: 186px; list-style: none;
    color: var(--text-light); font-size: 12.5px; line-height: 1.75;
  }
  .contact-list li, .phone { display: flex; align-items: center; gap: 7px; }
  .icon { width: 11px; height: 11px; flex: none; fill: var(--text-muted); }

  .world-map {
    position: absolute; left: 30px; top: 30px; width: 460px; height: 238px;
    background: radial-gradient(ellipse at center, var(--charcoal-light) 0%, rgba(90,90,93,0.35) 60%, transparent 80%);
  }
</style>
</head>
<body>

<section class="card card-front" aria-label="Business card front">
  <svg class="card-shape" viewBox="0 0 520 298" aria-hidden="true">
    <path d="M0 118 Q260 138 520 44 L520 60 Q260 150 0 130 Z" fill="var(--red)"/>
    <path d="M0 130 Q260 150 520 60 L520 298 L0 298 Z" fill="var(--charcoal)"/>
    <path d="M178 136 L200 136 L189 148 Z" fill="var(--red)"/>
  </svg>

  <div class="brand"><span class="brand-dot"></span>Velmora Builds</div>

  <div class="holder">
    <p class="holder-name">Daniel Hart</p>
    <p class="holder-title">President</p>
    <p class="phone">
      <svg class="icon" viewBox="0 0 24 24"><path d="M6.6 10.8a15 15 0 0 0 6.6 6.6l2.2-2.2a1 1 0 0 1 1-.25 11.4 11.4 0 0 0 3.6.6 1 1 0 0 1 1 1V20a1 1 0 0 1-1 1A17 17 0 0 1 3 4a1 1 0 0 1 1-1h3.5a1 1 0 0 1 1 1c0 1.25.2 2.45.6 3.6a1 1 0 0 1-.25 1z"/></svg>
      +974 55501234
    </p>
  </div>

  <div class="divider"></div>

  <ul class="contact-list">
    <li>
      <svg class="icon" viewBox="0 0 24 24"><path d="M2 5h20v14H2z M2 5l10 8 10-8" fill="none" stroke="var(--text-muted)" stroke-width="2"/></svg>
      info@velmora-builds.com
    </li>
    <li>
      <svg class="icon" viewBox="0 0 24 24"><circle cx="12" cy="12" r="9" fill="none" stroke="var(--text-muted)" stroke-width="2"/><path d="M3 12h18M12 3c3 3 3 15 0 18M12 3c-3 3-3 15 0 18" fill="none" stroke="var(--text-muted)" stroke-width="1.5"/></svg>
      www.velmora-builds.com
    </li>
    <li>P.O. Box 4120, West Bay Street, Doha - Qatar</li>
  </ul>
</section>

<section class="card card-back" aria-label="Business card back">
  <div class="world-map" role="img" aria-label="Faint dotted world map"></div>
  <div class="brand"><span class="brand-dot"></span>Velmora Builds</div>
</section>

</body>
</html>
```